QRV Stationery Design Project

Dear Designers,
We need a new stationery design for company to match our new logo.
Designers should provide a design for the following:
1. Business Card: 3.5x2 Inches.
2. Letterhead: A4 size.
3. Envelops: 25x35.5 Cm.
You can keep the Arabic name at the bottom of the logo Or you can use the separate attached Arabic Name.
Please refer to the attached logo guide for design information.
Sample Business Card information:
Name: Tariq Nawaf
Position: Operation Manager
Tel: +966 920007714 Ex. 500
Fax: +966 (3)8842617
Mob: +966 (5)00387251
email: tariq@qrv-example.com.sa
URL: www.qrv-example.com.sa
Address:
Al Wadi Tower, Suite 303
Nasser bin Salem Str.
Khobar, 31847
Saudi Arabia
Updates
Dear All,
Please note, we had uploaded our logo along with Arabic writing in Adobe illustrator format (.ai).
Regards,
Khalid
Dear All,
A sample data for the business card had been added as per your request.
Regards,
Khalid

```html
<!DOCTYPE html>
<html lang="en">
<head>
<meta charset="utf-8">
<title>QRV Stationery</title>
<link rel="stylesheet" href="https://fonts.googleapis.com/css2?family=Arimo:wght@400;700&family=Ubuntu:wght@400;700&display=swap">
<style>
:root{
  --board:#1b1b1b;
  --frame:#000;
  --navy:#0f1f5c;
  --grey:#8a9a9c;
  --paper:#fff;
  --ink:#1c1c2a;
}
*{margin:0;padding:0;box-sizing:border-box}
html,body{width:1149px;height:1200px;overflow:hidden;background:var(--frame)}
.board{position:absolute;left:8px;top:2px;width:1133px;height:1192px;background:var(--board)}
.sheet{position:absolute;background:var(--paper);box-shadow:2px 3px 8px rgba(0,0,0,.6)}
.card-front{left:385px;top:105px;width:191px;height:108px;background:var(--navy);display:flex;align-items:center;justify-content:center}
.wordmark{font-family:"Ubuntu",sans-serif;font-weight:700;color:var(--navy);letter-spacing:2px;line-height:1}
.card-front .wordmark{color:var(--paper);font-size:30px}
.card-back{left:596px;top:105px;width:190px;height:108px}
.person{position:absolute;left:13px;top:16px;font-family:"Arimo",sans-serif}
.person .name{font-weight:700;font-size:12px;color:#111}
.person .mob{font-size:5px;color:var(--ink);margin-top:2px;padding-left:26px}
.role{position:absolute;left:93px;top:20px;height:14px;border-left:1px solid #bbb;padding-left:3px;font-family:"Arimo",sans-serif;font-size:4.5px;color:#444;line-height:14px}
.art{position:absolute;bottom:0}
.contact{position:absolute;font-family:"Ubuntu",sans-serif;color:var(--ink);border-left:1px solid #9aa;line-height:1.25}
.contact li{list-style:none;display:flex;gap:6px;align-items:flex-start}
.contact svg{flex:none;fill:var(--navy)}
.contact .gap{margin-top:3px}
.letter-a4{left:33px;top:273px;width:536px;height:760px}
.letter-b{left:593px;top:326px;width:490px;height:636px}
.logo{position:absolute;display:flex;align-items:center;gap:10px}
.logo .dot{background:var(--navy)}
</style>
</head>
<body>
<div class="board">

  <div class="sheet card-front">
    <span class="wordmark">QRV</span>
  </div>

  <div class="sheet card-back">
    <div class="person">
      <div class="name">Tariq Nawaf</div>
      <div class="mob">+966 (5)00387251</div>
    </div>
    <div class="role">Operation Manager</div>
    <svg class="art" style="left:0" width="95" height="60" role="img" aria-label="Satellite and tracked truck illustration">
      <defs><linearGradient id="g1" x1="0" y1="0" x2="1" y2="1"><stop offset="0" stop-color="#fff"/><stop offset=".55" stop-color="#0f1f5c"/></linearGradient></defs>
      <rect width="95" height="60" fill="url(#g1)"/>
    </svg>
    <ul class="contact" style="left:108px;top:61px;font-size:4.8px;padding-left:4px">
      <li><svg width="6" height="5" viewBox="0 0 10 10"><path d="M5 0 10 5H8.5V10H1.5V5H0Z"/></svg><span>Al Wadi Tower, Suite 303<br>Nasser bin Salem Str.<br>Khobar, 31847, Saudi Arabia</span></li>
      <li class="gap"><svg width="6" height="5" viewBox="0 0 10 10"><path d="M2 0 4 3 3 4Q4 6 6 7L7 6 10 8 8 10Q0 8 0 2Z"/></svg><span>+966 920007714 Ex. 500</span></li>
      <li><svg width="6" height="5" viewBox="0 0 10 10"><rect x="0" y="4" width="10" height="6"/><rect x="2" y="0" width="6" height="4"/></svg><span>+966 (3)8842617</span></li>
      <li><svg width="6" height="5" viewBox="0 0 10 10"><rect y="2" width="10" height="7"/></svg><span>tariq@qrv-example.com.sa</span></li>
      <li><svg width="6" height="5" viewBox="0 0 10 10"><circle cx="5" cy="5" r="5"/></svg><span>www.qrv-example.com.sa</span></li>
    </ul>
  </div>

  <div class="sheet letter-a4">
    <div class="logo" style="left:26px;top:24px">
      <span class="dot" style="width:40px;height:40px"></span>
      <span class="wordmark" style="font-size:58px">QRV</span>
    </div>
    <svg class="art" style="left:270px" width="130" height="76" role="img" aria-label="Satellite and tracked truck illustration">
      <defs><linearGradient id="g2" x1="0" y1="0" x2="1" y2="1"><stop offset="0" stop-color="#fff"/><stop offset=".55" stop-color="#0f1f5c"/></linearGradient></defs>
      <rect width="130" height="76" fill="url(#g2)"/>
    </svg>
    <ul class="contact" style="left:411px;top:690px;font-size:7px;padding-left:5px">
      <li><svg width="8" height="7" viewBox="0 0 10 10"><path d="M5 0 10 5H8.5V10H1.5V5H0Z"/></svg><span>Al Wadi Tower, Suite 303<br>Nasser bin Salem Str.<br>Khobar, 31847, Saudi Arabia</span></li>
      <li class="gap"><svg width="8" height="7" viewBox="0 0 10 10"><path d="M2 0 4 3 3 4Q4 6 6 7L7 6 10 8 8 10Q0 8 0 2Z"/></svg><span>+966 920007714 Ex. 500</span></li>
      <li><svg width="8" height="7" viewBox="0 0 10 10"><rect x="0" y="4" width="10" height="6"/><rect x="2" y="0" width="6" height="4"/></svg><span>+966 (3)8842617</span></li>
      <li><svg width="8" height="7" viewBox="0 0 10 10"><rect y="2" width="10" height="7"/></svg><span>tariq@qrv-example.com.sa</span></li>
      <li><svg width="8" height="7" viewBox="0 0 10 10"><circle cx="5" cy="5" r="5"/></svg><span>www.qrv-example.com.sa</span></li>
    </ul>
  </div>

  <div class="sheet letter-b">
    <div class="logo" style="left:20px;top:30px">
      <span class="dot" style="width:36px;height:36px"></span>
      <span class="wordmark" style="font-size:52px">QRV</span>
    </div>
    <svg class="art" style="left:250px" width="122" height="76" role="img" aria-label="Satellite and tracked truck illustration">
      <defs><linearGradient id="g3" x1="0" y1="0" x2="1" y2="1"><stop offset="0" stop-color="#fff"/><stop offset=".55" stop-color="#0f1f5c"/></linearGradient></defs>
      <rect width="122" height="76" fill="url(#g3)"/>
    </svg>
    <ul class="contact" style="left:380px;top:572px;font-size:6.6px;padding-left:5px">
      <li><svg width="8" height="7" viewBox="0 0 10 10"><path d="M5 0 10 5H8.5V10H1.5V5H0Z"/></svg><span>Al Wadi Tower, Suite 303<br>Nasser bin Salem Str.<br>Khobar, 31847, Saudi Arabia</span></li>
      <li class="gap"><svg width="8" height="7" viewBox="0 0 10 10"><path d="M2 0 4 3 3 4Q4 6 6 7L7 6 10 8 8 10Q0 8 0 2Z"/></svg><span>+966 920007714 Ex. 500</span></li>
      <li><svg width="8" height="7" viewBox="0 0 10 10"><rect x="0" y="4" width="10" height="6"/><rect x="2" y="0" width="6" height="4"/></svg><span>+966 (3)8842617</span></li>
      <li><svg width="8" height="7" viewBox="0 0 10 10"><rect y="2" width="10" height="7"/></svg><span>tariq@qrv-example.com.sa</span></li>
      <li><svg width="8" height="7" viewBox="0 0 10 10"><circle cx="5" cy="5" r="5"/></svg><span>www.qrv-example.com.sa</span></li>
    </ul>
  </div>

</div>
</body>
</html>
```